Card for modern wood artisan that builds log homes and timber frames.

Design a card with catchy imagery. With a quick list of things I build and services I offer.

I'd like an English side and a french side. I can provide the text.

I am basically a guy that builds log homes and timber frames , but I am very eco friendly oriented.

I use only eco friendly products to limit my carbon footprint.
I want the client to feel as if they are hiring a good smart builder.

I have been building for a while but just starting out to market myself out there , not just work for other companies. Starting
My own thing legitimately.

I am very conscientious, and I take care of the work I do. I am trying to bring a new age, modern feel to an old profession.

Reason: I am not completely satisfied with A model yet, looking for that masculin rustic artistic design that I havent completely found yet. Thank you for your sumbissions.

Target Market(s)

People looking to hire a builder to design and build their projects.
And contractors that want to hire a quality subcontractor for their jobs.

Industry/Entity Type

Construction

Contact Information for Business Card

I want my logo on it, that I had designed here.
And a list of services I provide.

With my phone number, website adress and Email.

Requirements
Must have
• Artful presentation,
• Eco friendly feel
• I love trees.

```html
<!DOCTYPE html>
<html lang="en">
<head>
<meta charset="utf-8">
<title>Varden Wood Artisan – Business Card</title>
<link href="https://fonts.googleapis.com/css2?family=Oswald:wght@600&family=Open+Sans:wght@700;800&family=Bebas+Neue&display=swap" rel="stylesheet">
<style>
  :root {
    --page: #e9e6e0;
    --paper: #e4dccd;
    --ink: #1b1a17;
    --muted: #4a463f;
    --tree: #e9c43a;
    --tree-soft: #f1d76e;
    --grain: #2a2622;
  }
  * { box-sizing: border-box; margin: 0; padding: 0; }
  html, body { width: 974px; height: 1200px; overflow: hidden; background: var(--page); }
  .canvas { position: relative; width: 974px; height: 1200px; }

  .card {
    position: absolute; top: 140px; width: 420px; height: 720px;
    background: var(--paper); color: var(--ink);
    box-shadow: 0 6px 18px rgba(0,0,0,.18);
    overflow: hidden;
    font-family: "Open Sans", sans-serif;
  }
  .card--en { left: 47px; }
  .card--fr { left: 507px; }

  .badge { position: absolute; top: 0; left: 70px; width: 280px; height: 150px; }
  .badge svg { position: absolute; inset: 0; }
  .badge__name {
    position: absolute; top: 44px; width: 100%; text-align: center;
    font-family: "Oswald", sans-serif; font-weight: 600; font-size: 34px; letter-spacing: 1px;
  }
  .badge__year {
    position: absolute; top: 96px; width: 100%; text-align: center;
    font-family: "Oswald", sans-serif; font-weight: 600; font-size: 13px; color: var(--muted);
  }

  .services {
    position: absolute; top: 180px; width: 100%; text-align: center; list-style: none;
    font-weight: 800; font-size: 19px; line-height: 1.15; text-transform: uppercase;
  }
  .contact { position: absolute; top: 300px; width: 100%; text-align: center; }
  .contact__phone { font-weight: 800; font-size: 28px; }
  .contact__email { font-weight: 700; font-size: 19px; text-transform: uppercase; margin-top: 2px; }

  .tree-art {
    position: absolute; top: 390px; left: 70px; width: 280px; height: 270px;
    background: radial-gradient(ellipse at 50% 40%, var(--tree) 0%, var(--tree-soft) 55%, rgba(241,215,110,0) 72%);
  }

  .wordmark {
    position: absolute; top: 470px; left: 40px; width: 340px; height: 84px;
    border: 4px solid var(--ink); display: flex; align-items: center;
  }
  .wordmark__square { width: 84px; height: 100%; border-right: 4px solid var(--ink); }
  .wordmark__name {
    flex: 1; text-align: center;
    font-family: "Oswald", sans-serif; font-weight: 600; font-size: 48px; letter-spacing: 2px;
  }

  .website {
    position: absolute; bottom: 34px; width: 100%; text-align: center;
    font-weight: 800; font-size: 20px; text-transform: uppercase;
  }

  .grain-accent {
    position: absolute; top: 260px; right: 0; width: 46px; height: 110px;
    background: linear-gradient(90deg, var(--grain), #4b443c 50%, var(--grain));
    clip-path: polygon(40% 0, 100% 0, 100% 100%, 0 100%);
  }

  .side-label {
    position: absolute; top: 890px; width: 420px; text-align: center;
    font-family: "Bebas Neue", sans-serif; font-size: 44px; color: var(--ink); letter-spacing: 1px;
  }
  .side-label--en { left: 47px; }
  .side-label--fr { left: 507px; }
</style>
</head>
<body>
<main class="canvas">

  <article class="card card--en" lang="en">
    <div class="badge">
      <svg viewBox="0 0 280 150" width="280" height="150" aria-hidden="true">
        <polyline points="4,0 4,110 140,146 276,110 276,0" fill="none" stroke="#1b1a17" stroke-width="4"/>
      </svg>
      <div class="badge__name">NOEL VARDEN</div>
      <div class="badge__year">— 2017 —</div>
    </div>
    <ul class="services">
      <li>Carpentry Services</li>
      <li>Log Home</li>
      <li>Construction</li>
      <li>Timber Frame</li>
    </ul>
    <div class="contact">
      <div class="contact__phone">613.555.0142</div>
      <div class="contact__email">builder@vardenwood.com</div>
    </div>
    <div class="tree-art" role="img" aria-label="Yellow sketched tree illustration"></div>
    <div class="wordmark">
      <span class="wordmark__square"></span>
      <span class="wordmark__name">VARDEN</span>
    </div>
    <div class="website">www.vardenwood.com</div>
    <div class="grain-accent" role="img" aria-label="Black wood grain pattern"></div>
  </article>

  <article class="card card--fr" lang="fr">
    <div class="badge">
      <svg viewBox="0 0 280 150" width="280" height="150" aria-hidden="true">
        <polyline points="4,0 4,110 140,146 276,110 276,0" fill="none" stroke="#1b1a17" stroke-width="4"/>
      </svg>
      <div class="badge__name">NOEL VARDEN</div>
      <div class="badge__year">— 2017 —</div>
    </div>
    <ul class="services">
      <li>Services de menuiserie</li>
      <li>Maison de bois</li>
      <li>Construction</li>
      <li>Cadre en bois</li>
    </ul>
    <div class="contact">
      <div class="contact__phone">613.555.0142</div>
      <div class="contact__email">builder@vardenwood.com</div>
    </div>
    <div class="tree-art" role="img" aria-label="Illustration d'arbre jaune esquissé"></div>
    <div class="wordmark">
      <span class="wordmark__square"></span>
      <span class="wordmark__name">VARDEN</span>
    </div>
    <div class="website">www.vardenwood.com</div>
    <div class="grain-accent" role="img" aria-label="Motif de grain de bois noir"></div>
  </article>

  <div class="side-label side-label--en">English Side</div>
  <div class="side-label side-label--fr">French Side</div>

</main>
</body>
</html>
```